I will ask the design of the business card

We are looking for business card design of the new company "VORTELL PAYWORKS STUDIO LLC." Based in Azerbaijan.
In case
We are working on Azerbaijan to set up the first exchange of crypto currencies.

The key currency used in exchanges is called "MIRTA".
In case
We are doing project to make crypto currency infrastructure.

We provide state-of-the-art technology to the world.

```html
<!DOCTYPE html>
<html lang="en">
<head>
<meta charset="utf-8">
<title>Vortell Payworks Studio – Business Card</title>
<link href="https://fonts.googleapis.com/css2?family=Montserrat:wght@400;600;700&family=Roboto:wght@300;400&display=swap" rel="stylesheet">
<style>
  :root {
    --page: #ececec;
    --card: #f7f7f7;
    --brand-blue: #2a6fae;
    --brand-blue-dark: #225f98;
    --ink: #4a4a4a;
    --ink-soft: #6b6b6b;
    --rule: #b9b9b9;
    --white: #ffffff;
  }
  * { margin: 0; padding: 0; box-sizing: border-box; }
  html, body { width: 1200px; height: 1177px; overflow: hidden; }
  body {
    background: var(--page);
    font-family: "Roboto", Arial, sans-serif;
    position: relative;
  }
  .card {
    position: absolute;
    left: 170px;
    width: 860px;
    height: 491px;
    border-radius: 4px;
    box-shadow: 0 10px 30px rgba(0,0,0,0.12);
    overflow: hidden;
  }
  .card-front { top: 62px; background: var(--card); }
  .card-back { top: 624px; background: var(--brand-blue); }

  /* Front */
  .brand-block {
    position: absolute;
    left: 0; top: 0;
    width: 430px; height: 100%;
    display: flex; flex-direction: column;
    align-items: center; justify-content: center;
    gap: 26px;
  }
  .brand-dot {
    width: 92px; height: 92px;
    border-radius: 50%;
    background: var(--brand-blue);
  }
  .brand-name {
    font-family: "Montserrat", Arial, sans-serif;
    font-weight: 700;
    font-size: 22px;
    line-height: 1.3;
    color: var(--brand-blue);
    text-align: center;
    letter-spacing: 0.5px;
  }
  .divider {
    position: absolute;
    left: 430px; top: 140px;
    width: 1px; height: 210px;
    background: var(--rule);
  }
  .contact-block {
    position: absolute;
    left: 478px; top: 150px;
    color: var(--ink);
  }
  .person-name {
    font-family: "Montserrat", Arial, sans-serif;
    font-weight: 700;
    font-size: 30px;
    color: var(--brand-blue);
  }
  .person-role {
    font-size: 18px;
    color: var(--ink-soft);
    margin-top: 4px;
  }
  .address {
    font-size: 18px;
    line-height: 1.4;
    margin-top: 18px;
  }
  .contact-list {
    list-style: none;
    margin-top: 14px;
    font-size: 18px;
    line-height: 1.55;
  }
  .contact-list li { display: flex; align-items: center; gap: 12px; }
  .contact-list svg { width: 16px; height: 16px; flex: none; }

  /* Back */
  .network-backdrop {
    position: absolute; inset: 0;
    background: linear-gradient(135deg, var(--brand-blue) 0%, var(--brand-blue-dark) 100%);
  }
  .back-content {
    position: absolute; inset: 0;
    display: flex; flex-direction: column;
    align-items: center; justify-content: center;
    color: var(--white);
  }
  .mark-row { display: flex; align-items: center; gap: 22px; }
  .mark-dot { width: 70px; height: 70px; border-radius: 50%; background: var(--white); }
  .mark-name {
    font-family: "Roboto", Arial, sans-serif;
    font-weight: 300;
    font-size: 74px;
    letter-spacing: 6px;
    color: var(--white);
  }
  .tagline {
    margin-top: 22px;
    font-size: 20px;
    line-height: 1.35;
    text-align: center;
    font-weight: 400;
  }
</style>
</head>
<body>
  <section class="card card-front">
    <div class="brand-block">
      <div class="brand-dot"></div>
      <p class="brand-name">VORTELL PAYWORKS<br>STUDIO LLC.</p>
    </div>
    <div class="divider"></div>
    <div class="contact-block">
      <h1 class="person-name">Daniel ASTER</h1>
      <p class="person-role">Managing Director</p>
      <p class="address">AZ1010, 8/22 Lorin Str.<br>Baku City, Azerbaijan</p>
      <ul class="contact-list">
        <li>
          <svg viewBox="0 0 16 16" aria-hidden="true"><path d="M3 1.5l3 3-1.5 2c1 2 2.5 3.5 4.5 4.5l2-1.5 3 3-2 2C6 13.5 2.5 10 1 3.5z" fill="none" stroke="var(--brand-blue)" stroke-width="1.4"/></svg>
          000.000.0000
        </li>
        <li>
          <svg viewBox="0 0 16 16" aria-hidden="true"><rect x="4" y="1" width="8" height="14" rx="1.5" fill="none" stroke="var(--brand-blue)" stroke-width="1.4"/><circle cx="8" cy="12.5" r="0.9" fill="var(--brand-blue)"/></svg>
          000.000.0000
        </li>
        <li>
          <svg viewBox="0 0 16 16" aria-hidden="true"><rect x="1" y="3" width="14" height="10" fill="none" stroke="var(--brand-blue)" stroke-width="1.4"/><path d="M1 3l7 6 7-6" fill="none" stroke="var(--brand-blue)" stroke-width="1.4"/></svg>
          support@mirta.tech
        </li>
        <li>
          <svg viewBox="0 0 16 16" aria-hidden="true"><circle cx="8" cy="8" r="6.5" fill="none" stroke="var(--brand-blue)" stroke-width="1.3"/><ellipse cx="8" cy="8" rx="3" ry="6.5" fill="none" stroke="var(--brand-blue)" stroke-width="1.1"/><path d="M1.5 8h13M2.5 4.8h11M2.5 11.2h11" stroke="var(--brand-blue)" stroke-width="1.1"/></svg>
          www.mirta-tech.com
        </li>
      </ul>
    </div>
  </section>

  <section class="card card-back">
    <div class="network-backdrop" role="img" aria-label="Faint network mesh pattern of connected nodes across a blue background"></div>
    <div class="back-content">
      <div class="mark-row">
        <div class="mark-dot"></div>
        <h2 class="mark-name">MIRTA</h2>
      </div>
      <p class="tagline">Open digital asset trading network<br>for Modern Regional Commerce</p>
    </div>
  </section>
</body>
</html>
```